TL Ranch Sign

We are looking for a design that can be used outside of our ranch on a sign. Most likely metal outline sign but would be interested in full color design sign to put elsewhere. We want TL Ranch name incorporated in design. We have 2 photos of our dogs (remove background) that this name is based on and we would want them incorporated in design somehow!

```html
<!DOCTYPE html>
<html lang="en">
<head>
<meta charset="utf-8">
<title>TL Ranch Sign</title>
<link rel="stylesheet" href="https://fonts.googleapis.com/css2?family=Alfa+Slab+One&family=Staatliches&display=swap">
<style>
  :root {
    --page: #ffffff;
    --ink: #0b0b0b;
    --steel-dark: #5e5e5e;
    --steel-mid: #a9a9a9;
    --steel-light: #e4e4e4;
    --steel-pale: #f4f4f4;
    --screw-face: #f2f2f2;
    --screw-edge: #3a3a3a;
    --screw-slot: #2a2a2a;
    --kayak-red: #e8323f;
    --dog-brown: #6b4a35;
    --dog-cream: #e6d6b8;
  }
  html, body {
    margin: 0;
    padding: 0;
    width: 1200px;
    height: 778px;
    overflow: hidden;
    background: var(--page);
  }
  .canvas {
    position: relative;
    width: 1200px;
    height: 778px;
  }
  .sign-plate {
    position: absolute;
    left: 44px;
    top: 44px;
    width: 1074px;
    height: 679px;
    box-sizing: border-box;
    border: 1.5px solid var(--ink);
    background: linear-gradient(90deg, var(--steel-dark) 0%, var(--steel-light) 14%, var(--steel-mid) 32%, var(--steel-pale) 50%, var(--steel-mid) 70%, var(--steel-light) 86%, var(--steel-dark) 100%);
    box-shadow: 0 3px 4px rgba(0,0,0,0.35);
  }
  .sign-face {
    position: absolute;
    left: 15px;
    top: 19px;
    right: 15px;
    bottom: 22px;
    border: 3px solid var(--steel-pale);
    outline: 2px solid var(--steel-mid);
    background:
      repeating-linear-gradient(90deg, rgba(255,255,255,0.10) 0 2px, rgba(0,0,0,0.05) 2px 5px, rgba(255,255,255,0.06) 5px 9px),
      linear-gradient(90deg, #7d7d7d 0%, #d9d9d9 12%, #b5b5b5 30%, #cfcfcf 48%, #a8a8a8 66%, #d6d6d6 84%, #8a8a8a 100%);
    overflow: hidden;
  }
  .ranch-name,
  .ranch-address,
  .ranch-established {
    position: absolute;
    left: 0;
    right: 0;
    margin: 0;
    text-align: center;
    color: var(--ink);
    white-space: nowrap;
  }
  .ranch-name {
    top: 40px;
    height: 200px;
    line-height: 200px;
    font-family: "Alfa Slab One", serif;
    font-size: 190px;
    font-weight: 400;
    letter-spacing: 2px;
    transform: scaleX(0.63);
    transform-origin: 50% 50%;
  }
  .ranch-address {
    top: 222px;
    line-height: 1;
    font-family: "Staatliches", sans-serif;
    font-size: 78px;
    letter-spacing: 1px;
  }
  .ranch-established {
    top: 312px;
    line-height: 1;
    font-family: "Staatliches", sans-serif;
    font-size: 44px;
    letter-spacing: 0;
  }
  .screw {
    position: absolute;
    width: 37px;
    height: 37px;
  }
  .screw-top-left { left: 67px; top: 107px; }
  .screw-top-right { left: 960px; top: 107px; }
  .screw-bottom-left { left: 67px; top: 527px; }
  .screw-bottom-right { left: 960px; top: 527px; }
  .dogs-photo {
    position: absolute;
    left: 508px;
    top: 384px;
    width: 546px;
    height: 272px;
    background:
      linear-gradient(180deg, transparent 0%, transparent 71%, var(--kayak-red) 71%, var(--kayak-red) 100%),
      linear-gradient(90deg, transparent 0%, transparent 22%, var(--dog-brown) 30%, var(--dog-brown) 55%, var(--dog-cream) 62%, var(--dog-cream) 100%);
  }
</style>
</head>
<body>
<div class="canvas">
  <div class="sign-plate">
    <div class="sign-face">
      <h1 class="ranch-name">TL RANCH</h1>
      <p class="ranch-address">482 N CEDAR RIDGE RD</p>
      <p class="ranch-established">YEAR ESTABLISHED 2025</p>
    </div>
    <svg class="screw screw-top-left" viewBox="0 0 36 36" aria-hidden="true">
      <ellipse cx="18" cy="18" rx="16" ry="17" fill="var(--screw-face)" stroke="var(--screw-edge)" stroke-width="3"/>
      <path d="M10 10 L26 26 M26 10 L10 26" stroke="var(--screw-slot)" stroke-width="4"/>
    </svg>
    <svg class="screw screw-top-right" viewBox="0 0 36 36" aria-hidden="true">
      <ellipse cx="18" cy="18" rx="16" ry="17" fill="var(--screw-face)" stroke="var(--screw-edge)" stroke-width="3"/>
      <path d="M10 10 L26 26 M26 10 L10 26" stroke="var(--screw-slot)" stroke-width="4"/>
    </svg>
    <svg class="screw screw-bottom-left" viewBox="0 0 36 36" aria-hidden="true">
      <ellipse cx="18" cy="18" rx="16" ry="17" fill="var(--screw-face)" stroke="var(--screw-edge)" stroke-width="3"/>
      <path d="M10 10 L26 26 M26 10 L10 26" stroke="var(--screw-slot)" stroke-width="4"/>
    </svg>
    <svg class="screw screw-bottom-right" viewBox="0 0 36 36" aria-hidden="true">
      <ellipse cx="18" cy="18" rx="16" ry="17" fill="var(--screw-face)" stroke="var(--screw-edge)" stroke-width="3"/>
      <path d="M10 10 L26 26 M26 10 L10 26" stroke="var(--screw-slot)" stroke-width="4"/>
    </svg>
    <div class="dogs-photo" role="img" aria-label="Photo of the two ranch dogs, a brown and white shepherd and a cream labrador, sitting in a red kayak"></div>
  </div>
</div>
</body>
</html>
```